New Alcoholic Spiked Seltzer Line

We need a can design for a line of low calorie alcoholic seltzer. This product is a sparkling water and vodka drink with no sugar added in a slim 12 oz can.

This is a lighter, healthier, alternative to the sugary ready-to-drinks on the market. The product contains only 3 ingredients: Vodka, Water and Natural Flavors. It has only 100 calories but still has 5% alcohol, so you don't need to sacrifice alcohol to cut calories.

This product also does not contain any preservatives.

We want this design to communicate the following objectives to the consumer and in this order:

1. Appetizing product
2.Low calorie
3.Communicate the type of beverage (Spiked Seltzer)

The brand name of the product is VELKA.

The flavor of the product needed to be used for the design is Mango-Orange.

Comparable products are:

www.brisavelfizz.example/
https://www.tarnowbubble.example
https://quellrind.example/

The designs should not infringe or copy the creative directions of the products mentionned above. They are only given so that you can better understand the type of product we are developing.

Target Market(s)

Young Professional women between the ages of 25 and 44

Industry/Entity Type

Product

Colors

Designer to choose colors to be used in the design.

Requirements
Must have
• Design extendibility, meaning it can be adapted for other flavors.
• This is a new category in the market we are targeting, so consumers must easily be able to identify what type of product this is.

```html
<!DOCTYPE html>
<html lang="en">
<head>
<meta charset="utf-8">
<title>VELKA Seltzer – Mango Orange Can Label</title>
<link rel="stylesheet" href="https://fonts.googleapis.com/css2?family=Michroma&family=Marcellus&family=Cormorant+SC:wght@500&display=swap">
<style>
  :root {
    --page: #e6e6e8;
    --silver-dark: #b9bbbf;
    --silver-mid: #d7d8db;
    --silver-light: #f3f3f4;
    --orange: #f7a21b;
    --orange-deep: #f39419;
    --orange-light: #fbc02d;
    --white: #ffffff;
    --ink: #222222;
  }
  * { margin: 0; padding: 0; box-sizing: border-box; }
  html, body {
    width: 1200px; height: 1028px; overflow: hidden;
    background: var(--page);
  }
  .label {
    position: absolute; left: 80px; top: 94px;
    width: 1040px; height: 840px;
    background: linear-gradient(90deg, var(--silver-dark) 0%, var(--silver-light) 18%, var(--silver-mid) 35%, var(--silver-light) 55%, var(--silver-mid) 75%, var(--silver-light) 90%, var(--silver-dark) 100%);
    border-radius: 6px;
    overflow: hidden;
    box-shadow: 0 10px 30px rgba(0,0,0,0.18);
  }
  .label-shapes { position: absolute; inset: 0; }
  .claims-band {
    position: absolute; left: 0; top: 0; width: 100%; height: 78px;
    background: linear-gradient(90deg, var(--orange-deep), var(--orange-light) 50%, var(--orange-deep));
    display: flex; align-items: center; justify-content: center; gap: 22px;
    font-family: "Michroma", sans-serif; font-size: 20px; color: var(--white);
    letter-spacing: 1px;
  }
  .claims-band .dot { width: 14px; height: 14px; border-radius: 50%; background: var(--white); }
  .calorie-count {
    position: absolute; left: 300px; top: 360px; width: 200px;
    text-align: center; color: var(--white);
  }
  .calorie-count .number { font-family: "Marcellus", serif; font-size: 64px; line-height: 1; }
  .calorie-count .unit { font-family: "Michroma", sans-serif; font-size: 16px; margin-top: 6px; }
  .brand-block { position: absolute; left: 522px; top: 240px; color: var(--white); }
  .brand-name { font-family: "Michroma", sans-serif; font-size: 62px; line-height: 1; }
  .product-type { font-family: "Michroma", sans-serif; font-size: 32px; margin-top: 14px; }
  .flavor-name {
    position: absolute; left: 522px; top: 442px;
    font-family: "Michroma", sans-serif; font-size: 40px; line-height: 1.2; color: var(--white);
  }
  .volume-info {
    position: absolute; left: 370px; top: 700px; width: 300px;
    text-align: center; font-family: "Cormorant SC", serif; color: var(--ink);
  }
  .volume-info .abv { font-size: 26px; padding-bottom: 6px; border-bottom: 2px solid var(--ink); }
  .volume-info .size { font-size: 26px; padding-top: 6px; }
</style>
</head>
<body>
  <main class="label">
    <svg class="label-shapes" width="1040" height="840" viewBox="0 0 1040 840" aria-hidden="true">
      <defs>
        <linearGradient id="orange-disc" x1="0" y1="0" x2="1" y2="1">
          <stop offset="0" stop-color="#fbc02d"/>
          <stop offset="0.5" stop-color="#f7a21b"/>
          <stop offset="1" stop-color="#f39419"/>
        </linearGradient>
      </defs>
      <circle class="flavor-disc" cx="600" cy="410" r="260" fill="url(#orange-disc)"/>
      <path class="calorie-drop" fill="#d9dadd"
        d="M470,250 C455,300 495,340 495,410 A95,95 0 1 1 318,362 C350,300 420,285 470,250 Z"/>
    </svg>

    <div class="claims-band">
      <span>no sugar</span><span class="dot"></span>
      <span>no preservatives</span><span class="dot"></span>
      <span>vodka · water · natural flavors</span>
    </div>

    <div class="calorie-count">
      <div class="number">100</div>
      <div class="unit">calories</div>
    </div>

    <div class="brand-block">
      <div class="brand-name">VELKA</div>
      <div class="product-type">seltzer</div>
    </div>

    <div class="flavor-name">Mango<br>Orange</div>

    <div class="volume-info">
      <div class="abv">5% Alc.</div>
      <div class="size">12 fl oz (355ml)</div>
    </div>
  </main>
</body>
</html>
```